IT Network Consultancy - Brochure

m2 relays is a IT network consultancy based in London. We're looking for a smart, modern and professional brochure in A4 format. Our website is here: www.m2relays.co.uk. We likely will require the brochure in two formats:

PDF / Scroll Down (The most common distribution of the brochure will be PDF, which will scroll down page after page):

Page 1 - Front page
Page 2 - Portrait / scroll down
Page 3 - Portrait / scroll down
Page 4 - Portrait / scroll down
Page 5 - Portrait / scroll down
Page 6 - Back page

Side by Side / Professionally Printed:

Page 1 - Front page
Page 2/3 - Side by side
Page 4/5 - Side by side
Page 6 - Back page
Updates

Please note - I made a number of changes to the design brief after initially submitting it.

I have also increased the first prize budget from £150 to £200 (US $327)

Images may be used - no pictures of people though or anything too bright...

Reason: We're extending the deadline as we haven't received as many designs as we'd liked (one so far!)

Following a question from another designer:

We're a technology consultancy, not a technology company.  We don't need any futuristic graphics, just something that looks clean and professional.  Almost along the lines of financial services but not to traditional.

Target Market(s)

Large enterprise / global companies / corporates

Industry/Entity Type

Distribution

Requirements
Must have
• Incorporate our logo - which is attached to the project. They are in AI format (can be opened in Inkscape).

Initially the brochure is to be used specifically for our company profile / fact sheet (see attached PPT for text).

We would like to have a template we can also use for future documents.

Fonts should be simple.
Nice to have
• The project does not have to conform to the colour of our website but this should give you inspiration of the style we like.

A way to incorporate the design into MS PowerPoint, i.e. a template for corporate presentations.
Should not have
• Bright colours.

```html
<!DOCTYPE html>
<html lang="en">
<head>
<meta charset="utf-8">
<title>m2 relays – Brochure Back Page</title>
<link rel="stylesheet" href="https://fonts.googleapis.com/css2?family=Questrial&family=Lato:wght@400&display=swap">
<style>
  :root {
    --backdrop: #c9c9c9;
    --page: #323d46;
    --ink: #c8cdd1;
    --ink-soft: #9aa3aa;
    --rule: #7e878e;
  }
  * { margin: 0; padding: 0; box-sizing: border-box; }
  html, body {
    width: 1200px; height: 900px; overflow: hidden;
    background: var(--backdrop);
  }
  .back-page {
    position: absolute; left: 302px; top: 25px;
    width: 601px; height: 850px;
    background: var(--page);
    overflow: hidden;
  }
  .stripe-field {
    position: absolute; left: 0; width: 290px; height: 302px;
  }
  .stripe-field--top {
    top: 18px;
    background: linear-gradient(to right, rgba(200,206,211,0.30), rgba(200,206,211,0.10) 55%, rgba(50,61,70,0)),
                linear-gradient(to bottom, rgba(50,61,70,0.6), rgba(50,61,70,0));
    background-blend-mode: normal;
  }
  .stripe-field--bottom {
    top: 530px;
    background: linear-gradient(to right, rgba(200,206,211,0.30), rgba(200,206,211,0.10) 55%, rgba(50,61,70,0)),
                linear-gradient(to top, rgba(50,61,70,0.6), rgba(50,61,70,0));
  }
  .dividers { position: absolute; left: 0; top: 0; }
  .globe-area {
    position: absolute; left: 120px; top: 338px;
    width: 180px; height: 182px; border-radius: 50%;
    background: radial-gradient(circle at 55% 45%, rgba(150,160,168,0.24), rgba(150,160,168,0.07) 65%, rgba(50,61,70,0) 72%);
  }
  .contact-block {
    position: absolute; left: 367px; top: 369px;
    height: 105px; padding-left: 14px;
    border-left: 1px solid var(--rule);
    font-family: "Lato", sans-serif; color: var(--ink);
  }
  .brand-name {
    font-family: "Questrial", sans-serif; font-weight: 400;
    font-size: 21px; letter-spacing: 1.5px;
    color: var(--ink); text-transform: uppercase;
    line-height: 1; margin-top: 8px; margin-bottom: 12px;
  }
  .contact-list { list-style: none; font-size: 10.5px; }
  .contact-list li { display: flex; height: 19px; align-items: center; }
  .contact-label { width: 50px; color: var(--ink-soft); }
</style>
</head>
<body>
  <main class="back-page">
    <div class="stripe-field stripe-field--top" role="img" aria-label="Decorative field of fine silver horizontal stripes fading to the right"></div>
    <div class="stripe-field stripe-field--bottom" role="img" aria-label="Decorative field of fine silver horizontal stripes fading to the right"></div>

    <svg class="dividers" width="601" height="850" viewBox="0 0 601 850" aria-hidden="true">
      <defs>
        <linearGradient id="fade-both">
          <stop offset="0" stop-color="#ffffff" stop-opacity="0.1"/>
          <stop offset="0.5" stop-color="#ffffff" stop-opacity="0.9"/>
          <stop offset="1" stop-color="#ffffff" stop-opacity="0"/>
        </linearGradient>
      </defs>
      <rect class="divider" x="0" y="327" width="580" height="2" fill="url(#fade-both)"/>
      <rect class="divider" x="0" y="521" width="580" height="2" fill="url(#fade-both)"/>
    </svg>

    <div class="globe-area" role="img" aria-label="Faint dotted globe showing Europe and Africa"></div>

    <section class="contact-block">
      <h1 class="brand-name">m2 relays</h1>
      <ul class="contact-list">
        <li><span class="contact-label">phone</span><span>: +44 (0) 2085 550143</span></li>
        <li><span class="contact-label">mobile</span><span>: +44 (0) 7700 900418</span></li>
        <li><span class="contact-label">email</span><span>: info@m2relays.co.uk</span></li>
      </ul>
    </section>
  </main>
</body>
</html>
```